The Ironfield Trials Puerto Rico (TFTR) – Sponsorship Proposal 2026 | Second Edition

We are looking to redesign and elevate our Sponsorship Proposal for the second edition of The Ironfield Trials Puerto Rico (TFTR) - a Tactical Fitness competition that combines functional fitness and live-fire shooting in a safe and controlled environment.
The first edition (March 7, 2026) was a proven success, and the updated proposal must reflect that evolution from concept to validated event.
OBJECTIVE
Create a visually striking, premium, and highly structured sponsorship proposal that communicates:
- Credibility (proven event)
- Growth (scaling momentum)
- Experience (not just competition, but a full event)
----------------------------
KEY DATA TO INCLUDE (VERY IMPORTANT)
The design must highlight the following real metrics prominently:
- 96 registered athletes
- 240+ spectators
- 35 volunteers
- 370+ total attendees
- 14 female athletes
- 5 youth participants (ages 12–16)
- $3,300 awarded in prize money
INAUGURAL SPONSORS:
- Coastal Sky Corps
- Borinquen Highland Defense Reserve
- Northern Land Militia
- Cedarcrest Real Estate
- MVT (Mochila Vida Threads)
- Tidelark Studio
- Harbor Pulse 939, KORVA San Juan
- Premier Logistics PR
- Core Tempo
NEXT EVENT (IMPORTANT FOR DESIGN STORY)
- Event Date: December 19, 2026
- Expected Attendance:
- 130+ athletes
- 300+ spectators
- ~500 total attendees
- Theme: Christmas Experience
- Full event decorated in Christmas theme
- Food vendors + traditional Puerto Rican roasted pork (150+ lbs), community, and sponsor activations
👉 This is NOT just a competition - it is an experience-driven event.
STRUCTURE (BASED ON CURRENT PROPOSAL)
- Use the existing proposal as structural reference , but improve layout, hierarchy, and storytelling:
- Cover Page (modern + bold)
- Executive Summary (UPDATED with real results)
- Event Concept / Experience
- Audience & Attendance (with real + projected numbers)
- Sponsors (social proof section)
- Sponsorship Packages (Alpha = $10,000, Bravo = $1,000, Charlie = $500, Delta = $250)
- Why Sponsor TFTR
- Contact Page
EVENT DIVISIONS (UPDATED – VERY IMPORTANT)
The proposal must clearly showcase the five official competition divisions, with strong visual hierarchy (icons, images, or cards per division). This section should feel dynamic, premium, and easy to scan.
Divisions to include:
SCALE DIVISION (Adaptive)
An adaptive division for those who want to experience TFTR in a controlled environment.
No rankings. No prizes.
This is about completing the challenge.
BEGINNER DIVISION
For athletes ready to compete in a structured and approachable format.
Challenging, but accessible.
Athletes compete for placement.
INTERMEDIATE DIVISION
For athletes with a strong foundation in fitness and shooting.
Heavier loads. Higher standards.
Performance matters.
JÍBARO DIVISION (Elite)
The highest level of competition at TFTR.
Retention holsters required. Rifles carried in slings. Heavier loads.
Built for athletes who want to prove themselves.
MASTERS 45+ DIVISION
For athletes 45+ who want to compete while prioritizing longevity and control.
Maintains competitive intensity within an age-based category.
2-GUN FORMAT (IMPORTANT – INCLUDE BELOW DIVISIONS)
All divisions are available in either:
Pistol
2-Gun (Pistol + Rifle)
In the 2-Gun format, athletes utilize both pistol and rifle throughout the competition, transitioning between weapons under physical fatigue and time pressure.
DESIGN NOTE FOR THIS SECTION
Present divisions as individual visual blocks/cards (like the reference provided)
Use bold titles + short descriptions (keep text tight)
Include action images per division if possible
Highlight Jíbaro Division as the elite tier visually
Ensure this section is one of the most visually engaging pages in the proposal
DESIGN STYLE & VISUAL DIRECTION
We want a military / tactical / premium fitness aesthetic, similar to brands like:
- Brackett Athletics
- The Ranger Trials
- MoveLoop-style event decks
Tone:
- Strong
- Clean
- Masculine but modern
- Minimal clutter
COLOR PALETTE (MANDATORY)
Use the following brand colors:
- Light Olive Green (#636B2F)
- Dark Olive Green (#3D4127)
- Sand / Khaki (#C2B280)
- Charcoal / Black (#1C1C1C)
- Light Gray (#D3D3D3)
- White (#FFFFFF)
- Accent Red (#C80018) – for highlights only
DESIGN NOTES
- Use bold typography (military/tactical feel - I will include the font called BOOTCAMP which is the main font used for the first edition)
- Strong use of contrast (dark backgrounds + light text)
- Icons for stats (athletes, spectators, etc.)
- Clean infographics for numbers
- Full-page images for impact (action shots, athletes, shooting, fitness)
- Official logo included (PNG and vectorized)
- Keep it visually dynamic but easy to read
IMPORTANT MESSAGE SHIFT
The proposal must clearly communicate:
- This is NOT a new event
- This is a proven concept that is scaling
Before: “Support us”
Now: “Join a growing movement early”
FINAL DELIVERABLE
- Print-ready PDF (high quality)
- Editable source file (Illustrator)
- Modern, clean layout with strong visual hierarchy
Website: www.theironfieldtrials.example
Instagram: https://www.instagram.com/theironfieldtrials/
Fitness and Shooting Sports
- BOOTCAMP

```html
<!DOCTYPE html>
<html lang="en">
<head>
<meta charset="UTF-8">
<title>The Ironfield Trials Puerto Rico – Sponsorship Proposal 2026</title>
<link href="https://fonts.googleapis.com/css2?family=Bebas+Neue&family=Inter:ital,wght@0,400;0,600;0,700;1,400;1,500&display=swap" rel="stylesheet">
<style>
  :root {
    --olive: #636B2F;
    --olive-dark: #3D4127;
    --sand: #C2B280;
    --sand-light: #D8CB9C;
    --charcoal: #1C1C1C;
    --black: #050505;
    --gray: #D3D3D3;
    --board: #B8B8B8;
    --white: #FFFFFF;
    --card: #2E2E2C;
    --display: "Bebas Neue", "Oswald", sans-serif;
    --body: "Inter", "Helvetica Neue", Arial, sans-serif;
  }
  * { box-sizing: border-box; margin: 0; padding: 0; }
  html, body { width: 1019px; height: 1200px; overflow: hidden; }
  body { background: var(--board); position: relative; font-family: var(--body); }

  .page {
    position: absolute; width: 398px; height: 514px;
    background: var(--black); overflow: hidden; color: var(--white);
  }
  .page--cover { left: 69px; top: 76px; }
  .page--summary { left: 483px; top: 76px; }
  .page--experience { left: 69px; top: 610px; }

  .abs { position: absolute; }
  .display { font-family: var(--display); font-weight: 400; letter-spacing: 0.2px; line-height: 0.95; }

  /* Cover */
  .cover-photo {
    position: absolute; inset: 0;
    background:
      radial-gradient(ellipse 70% 60% at 62% 45%, #4a4a46 0%, #2c2c2a 45%, rgba(10,10,10,0) 80%),
      linear-gradient(180deg, #1f211c 0%, #2a2a27 40%, #111 75%, #050505 100%);
  }
  .cover-badge {
    left: 141px; top: 29px; width: 106px; height: 106px; border-radius: 50%;
    background: var(--black); display: flex; align-items: center; justify-content: center;
  }
  .cover-badge__ring {
    width: 90px; height: 90px; border-radius: 50%; border: 1.5px solid var(--white);
    display: flex; align-items: center; justify-content: center; text-align: center;
    font-family: var(--display); font-size: 13px; line-height: 1; color: var(--white);
  }
  .cover-title { left: 0; width: 100%; text-align: center; }
  .cover-title--the { top: 246px; font-size: 28px; }
  .cover-title--main { top: 277px; font-size: 41px; }
  .cover-title--place { top: 318px; font-size: 41px; color: var(--sand); }
  .cover-tag {
    left: 72px; top: 369px; width: 253px; height: 31px; background: var(--olive);
    display: flex; align-items: center; justify-content: center;
    font-family: var(--display); font-size: 23px; color: var(--sand-light); padding-top: 2px;
  }
  .cover-lead {
    left: 0; width: 100%; top: 409px; text-align: center;
    font-style: italic; font-weight: 500; font-size: 11px;
  }
  .cover-meta {
    left: 0; width: 100%; top: 445px; display: flex; justify-content: center; align-items: center;
    gap: 8px; font-family: var(--display); font-size: 14px;
  }
  .cover-meta__item { display: flex; align-items: center; gap: 6px; }
  .cover-meta__divider { width: 1px; height: 12px; background: var(--gray); margin: 0 8px; }

  /* Section band */
  .section-band {
    left: 0; height: 22px; display: flex; align-items: center;
    background: var(--olive); color: var(--sand-light);
    font-family: var(--display); font-size: 15px; padding: 2px 0 0 28px;
  }
  .section-band__slashes { position: absolute; top: 0; }

  .headline { left: 28px; font-size: 30px; color: var(--sand); line-height: 0.93; }
  .body-copy { font-size: 7.6px; line-height: 10.4px; color: var(--white); }
  .body-copy strong { color: var(--sand); font-weight: 600; }
  .label-heading { font-family: var(--display); font-size: 13px; color: var(--sand); }

  /* Summary */
  .summary-photo {
    left: 218px; top: 28px; width: 152px; height: 250px; border-radius: 7px;
    background: linear-gradient(160deg, #4f5a3a 0%, #6b6a52 35%, #8a7d62 65%, #a59476 100%);
  }
  .stats { left: 28px; top: 302px; display: flex; gap: 4px; }
  .stat {
    height: 99px; background: var(--card); border: 0.7px solid #4a4a46; border-radius: 2px;
    display: flex; flex-direction: column; align-items: center; padding-top: 9px; text-align: center;
  }
  .stat__value { font-family: var(--display); font-size: 22px; color: var(--sand); margin-top: 6px; line-height: 1; }
  .stat__label { font-size: 6.3px; line-height: 7.6px; color: var(--gray); margin-top: 3px; }
  .closing { left: 93px; top: 424px; font-size: 23px; line-height: 0.98; }
  .closing__line--sand { color: var(--sand); }
  .closing__line--olive { color: var(--olive); }

  /* Experience */
  .athlete-photo {
    left: 240px; top: 17px; width: 140px; height: 240px;
    background: radial-gradient(ellipse 55% 60% at 50% 45%, #2e2e2c 0%, #1c1c1c 55%, rgba(5,5,5,0) 100%);
  }
  .subhead { left: 28px; top: 128px; font-size: 22px; color: var(--olive); }
  .tests { left: 28px; top: 217px; display: flex; gap: 7px; }
  .test {
    width: 58px; height: 67px; border: 0.8px solid #8a8a80; border-radius: 6px;
    display: flex; flex-direction: column; align-items: center; justify-content: space-between;
    padding: 12px 2px 8px; font-size: 6.5px; line-height: 7.8px; text-align: center; color: var(--white);
  }
  .edition {
    left: 28px; top: 308px; width: 341px; height: 162px; border-radius: 8px;
    background: var(--olive); overflow: hidden;
  }
  .edition__photo {
    position: absolute; left: 0; top: 0; width: 156px; height: 100%;
    background: linear-gradient(150deg, #6f6a55 0%, #4c4a3e 45%, #2b2b28 100%);
  }
  .edition__kicker { left: 172px; top: 14px; font-size: 13px; color: var(--sand-light); }
  .edition__title { left: 172px; top: 27px; font-size: 23px; color: var(--sand-light); }
  .edition__list { left: 205px; top: 56px; list-style: none; font-size: 7.6px; line-height: 9.2px; text-transform: uppercase; }
  .edition__list li { margin-bottom: 9px; }
  .edition__list li:nth-child(3) { margin-bottom: 11px; }
  .footer-line { left: 0; width: 100%; top: 481px; text-align: center; font-size: 12px; color: var(--sand); }
</style>
</head>
<body>

<!-- Cover -->
<section class="page page--cover">
  <div class="cover-photo" role="img" aria-label="Photo of an athlete aiming a rifle on the range, wearing cap and ear protection"></div>
  <div class="abs cover-badge">
    <div class="cover-badge__ring">THE IRONFIELD<br>TRIALS<br>PUERTO RICO</div>
  </div>
  <div class="abs display cover-title cover-title--the">THE</div>
  <div class="abs display cover-title cover-title--main">IRONFIELD TRIALS</div>
  <div class="abs display cover-title cover-title--place">PUERTO RICO</div>
  <div class="abs cover-tag">SPONSORSHIP PROPOSAL 2026</div>
  <p class="abs cover-lead">A Proven Tactical Fitness Experience — Now Scaling</p>
  <div class="abs cover-meta">
    <span class="cover-meta__item">
      <svg width="11" height="13" viewBox="0 0 11 13" fill="none" stroke="#fff" stroke-width="0.9"><path d="M5.5 12s4-4.2 4-7A4 4 0 0 0 1.5 5c0 2.8 4 7 4 7z"/><circle cx="5.5" cy="5" r="1.5"/></svg>
      Puerto Rico
    </span>
    <span class="cover-meta__divider"></span>
    <span class="cover-meta__item">
      <svg width="15" height="13" viewBox="0 0 15 13" fill="none" stroke="#fff" stroke-width="0.9"><rect x="0.5" y="1.5" width="11" height="10" rx="1"/><line x1="0.5" y1="4" x2="11.5" y2="4"/><line x1="3" y1="0.5" x2="3" y2="2.5"/><line x1="9" y1="0.5" x2="9" y2="2.5"/><circle cx="11.5" cy="9.5" r="2.8" fill="#050505"/><path d="M11.5 8v1.5h1"/></svg>
      December 19, 2026
    </span>
  </div>
</section>

<!-- Executive summary: results -->
<section class="page page--summary">
  <div class="abs section-band" style="top:28px;width:137px;">EXECUTIVE SUMMARY</div>
  <svg class="abs section-band__slashes" style="left:137px;top:28px;" width="30" height="22" viewBox="0 0 30 22"><polygon points="0,0 10,0 0,22" fill="#636B2F"/><polygon points="11,0 15,0 6,22 2,22" fill="#636B2F"/><polygon points="20,0 24,0 15,22 11,22" fill="#636B2F"/></svg>
  <h1 class="abs display headline" style="top:67px;">FROM CONCEPT TO<br>PROVEN EVENT</h1>
  <p class="abs body-copy" style="left:28px;top:139px;width:172px;">The Ironfield Trials Puerto Rico (TFTR) successfully launched its inaugural edition on <strong>March 7, 2026</strong>, establishing itself as a unique tactical fitness competition combining functional training and live-fire shooting in a safe, structured environment.</p>
  <p class="abs body-copy" style="left:28px;top:211px;width:160px;">What began as a concept is now a <strong>validated and growing event platform.</strong></p>
  <div class="abs summary-photo" role="img" aria-label="Photo of an athlete pulling a weighted sled on a dirt course"></div>

  <div class="abs label-heading" style="left:28px;top:276px;">IN JUST ONE EDITION, TFTR DELIVERED:</div>
  <div class="abs stats">
    <div class="stat" style="width:40px;"><svg width="24" height="20" viewBox="0 0 24 20" fill="none" stroke="#fff" stroke-width="0.9"><circle cx="9" cy="10" r="7"/><circle cx="17" cy="7" r="4"/><circle cx="17" cy="7" r="1.5"/></svg><span class="stat__value">96</span><span class="stat__label">Registered<br>Athletes</span></div>
    <div class="stat" style="width:48px;"><svg width="24" height="20" viewBox="0 0 24 20" fill="none" stroke="#fff" stroke-width="0.9"><circle cx="9" cy="10" r="7"/><circle cx="17" cy="7" r="4"/><circle cx="17" cy="7" r="1.5"/></svg><span class="stat__value">240+</span><span class="stat__label">Spectators</span></div>
    <div class="stat" style="width:38px;"><svg width="24" height="20" viewBox="0 0 24 20" fill="none" stroke="#fff" stroke-width="0.9"><circle cx="9" cy="10" r="7"/><circle cx="17" cy="7" r="4"/><circle cx="17" cy="7" r="1.5"/></svg><span class="stat__value">35</span><span class="stat__label">Volunteers</span></div>
    <div class="stat" style="width:46px;"><svg width="24" height="20" viewBox="0 0 24 20" fill="none" stroke="#fff" stroke-width="0.9"><circle cx="9" cy="10" r="7"/><circle cx="17" cy="7" r="4"/><circle cx="17" cy="7" r="1.5"/></svg><span class="stat__value">370+</span><span class="stat__label">Total<br>Attendees</span></div>
    <div class="stat" style="width:38px;"><svg width="24" height="20" viewBox="0 0 24 20" fill="none" stroke="#fff" stroke-width="0.9"><circle cx="9" cy="10" r="7"/><circle cx="17" cy="7" r="4"/><circle cx="17" cy="7" r="1.5"/></svg><span class="stat__value">14</span><span class="stat__label">Female<br>Athletes</span></div>
    <div class="stat" style="width:47px;"><svg width="24" height="20" viewBox="0 0 24 20" fill="none" stroke="#fff" stroke-width="0.9"><circle cx="9" cy="10" r="7"/><circle cx="17" cy="7" r="4"/><circle cx="17" cy="7" r="1.5"/></svg><span class="stat__value">5</span><span class="stat__label">Youth<br>Participants<br>(Ages 12–16)</span></div>
    <div class="stat" style="width:57px;"><svg width="24" height="20" viewBox="0 0 24 20" fill="none" stroke="#fff" stroke-width="0.9"><circle cx="9" cy="10" r="7"/><circle cx="17" cy="7" r="4"/><circle cx="17" cy="7" r="1.5"/></svg><span class="stat__value">$3,300</span><span class="stat__label">Awarded in<br>Prize Money</span></div>
  </div>

  <div class="abs display closing">
    <div class="closing__line--sand">TFTR IS NO LONGER AN IDEA</div>
    <div class="closing__line--olive">IT IS A GROWING MOVEMENT.</div>
  </div>
</section>

<!-- Executive summary: experience -->
<section class="page page--experience">
  <div class="abs section-band" style="top:29px;width:133px;">EXECUTIVE SUMMARY</div>
  <svg class="abs section-band__slashes" style="left:133px;top:29px;" width="30" height="22" viewBox="0 0 30 22"><polygon points="0,0 10,0 0,22" fill="#636B2F"/><polygon points="11,0 15,0 6,22 2,22" fill="#636B2F"/><polygon points="20,0 24,0 15,22 11,22" fill="#636B2F"/></svg>
  <div class="abs athlete-photo" role="img" aria-label="Photo of an athlete in a black hoodie carrying a rifle and pistol"></div>
  <h2 class="abs display headline" style="top:66px;">MORE THAN A<br>COMPETITION</h2>
  <div class="abs display subhead">A TACTICAL EXPERIENCE</div>
  <p class="abs body-copy" style="left:28px;top:155px;width:200px;">TFTR blends functional fitness, tactical skill, and community into one immersive event.</p>
  <div class="abs label-heading" style="left:28px;top:196px;">ATHLETES ARE TESTED ACROSS:</div>
  <div class="abs tests">
    <div class="test"><svg width="24" height="20" viewBox="0 0 24 20" fill="none" stroke="#fff" stroke-width="0.9"><circle cx="9" cy="10" r="7"/><circle cx="17" cy="7" r="4"/><circle cx="17" cy="7" r="1.5"/></svg><span>Strength</span></div>
    <div class="test"><svg width="24" height="20" viewBox="0 0 24 20" fill="none" stroke="#fff" stroke-width="0.9"><circle cx="9" cy="10" r="7"/><circle cx="17" cy="7" r="4"/><circle cx="17" cy="7" r="1.5"/></svg><span>Endurance</span></div>
    <div class="test"><svg width="24" height="20" viewBox="0 0 24 20" fill="none" stroke="#fff" stroke-width="0.9"><circle cx="9" cy="10" r="7"/><circle cx="17" cy="7" r="4"/><circle cx="17" cy="7" r="1.5"/></svg><span>Precision<br>under fatigue</span></div>
    <div class="test"><svg width="24" height="20" viewBox="0 0 24 20" fill="none" stroke="#fff" stroke-width="0.9"><circle cx="9" cy="10" r="7"/><circle cx="17" cy="7" r="4"/><circle cx="17" cy="7" r="1.5"/></svg><span>Tactical<br>decision-making</span></div>
  </div>
  <p class="abs body-copy" style="left:28px;top:291px;">But TFTR goes beyond competition.</p>

  <div class="abs edition">
    <div class="edition__photo" role="img" aria-label="Photo of competitors firing rifles at the shooting line"></div>
    <div class="abs display edition__kicker">THE 2026 EDITION</div>
    <div class="abs display edition__title">INTRODUCES:</div>
    <ul class="abs edition__list">
      <li>Full Christmas-themed<br>event environment</li>
      <li>Food vendors +<br>traditional Puerto Rican<br>roasted pork (150+ lbs)</li>
      <li>Community activations</li>
      <li>Sponsor engagement zones</li>
    </ul>
  </div>

  <div class="abs display footer-line">THIS IS DESIGNED AS AN EXPERIENCE-DRIVEN EVENT, NOT JUST A COMPETITION.</div>
</section>

</body>
</html>
```